Prestige Car Bodyshop Business Card

We are a car bodyshop based in the UK. Our customer base is mainly prestige high-value vehicles. I am looking for a classy and stylish business card design for my staff to give out to customers, with their direct email and phone number, as well as our main email and phone number with address details

I am also looking to have a general business card design with just our main company address and contact details, but also have a space to add a manufacturer approval logo (i.e Velmora, Orek, Tovalo etc... logo) in the corner somewhere.

I do not particularly want any outlines or pictures of cars on the card, I would just like a quality high-end look.

Please feel free to get in touch if you have any questions or queries?

Many Thanks

Malcolm

Target Market(s)

Prestige vehicle owners

Industry/Entity Type

Automotive

Contact Information for Business Card

I am looking for a classy and stylish business card design for my staff to give out to customers, with their direct email and phone number, as well as our main email and phone number with address details

Font styles to use
Sans Serif

Colors

Designer to choose colors to be used in the design.

Requirements
Nice to have
• I do not particularly want any outlines or pictures of cars on the card, I would just like a quality high-end look.

```html
<!DOCTYPE html>
<html lang="en">
<head>
<meta charset="utf-8">
<title>Harlow Accident Repair Centre – Business Cards</title>
<link href="https://fonts.googleapis.com/css2?family=Open+Sans:wght@300;400;600;700&display=swap" rel="stylesheet">
<style>
  :root {
    --stage: #e9e6e1;
    --paper: #ffffff;
    --paper-shade: #eeeeef;
    --navy: #22428f;
    --navy-deep: #1b3577;
    --azure: #1f7fc9;
    --azure-light: #1e96d6;
    --orange: #f0962a;
    --orange-deep: #d97a12;
    --ink-logo: #3c55a3;
    --white: #ffffff;
  }
  * { box-sizing: border-box; margin: 0; padding: 0; }
  html, body { width: 1200px; height: 1023px; overflow: hidden; }
  body {
    background: var(--stage);
    font-family: "Open Sans", Arial, sans-serif;
    position: relative;
  }
  .card {
    position: absolute;
    width: 680px;
    height: 388px;
    border-radius: 18px;
    overflow: hidden;
    box-shadow: 0 14px 30px rgba(0,0,0,.22);
  }

  /* ---------- Staff card (front) ---------- */
  .card--staff {
    left: 50px; top: 50px;
    background: linear-gradient(180deg, var(--paper) 0%, var(--paper-shade) 100%);
  }
  .makers {
    position: absolute; top: 22px; right: 30px;
    display: flex; gap: 22px; align-items: center;
    font-size: 12px; letter-spacing: 2px; color: #6f6f74; text-transform: uppercase;
  }
  .brand {
    position: absolute; left: 58px; top: 70px;
    display: flex; align-items: center; gap: 26px;
  }
  .brand__disc {
    width: 122px; height: 122px; border-radius: 50%;
    background: radial-gradient(circle at 35% 35%, var(--azure-light), var(--azure));
  }
  .brand__name {
    font-weight: 300; font-size: 62px; letter-spacing: 1px; line-height: 1;
    color: var(--ink-logo);
  }
  .brand__rule { height: 2px; background: var(--ink-logo); margin: 8px 0 6px; width: 330px; }
  .brand__tagline {
    font-weight: 400; font-size: 17px; letter-spacing: 1px; color: var(--ink-logo);
  }
  .band {
    position: absolute; left: 0; right: 0; bottom: 0; height: 152px;
    background: linear-gradient(100deg, #3f63a8 0%, var(--navy) 45%, var(--navy-deep) 100%);
    color: var(--white);
  }
  .band__accent { position: absolute; top: -8px; width: 120px; height: 22px; }
  .band__accent--left { left: 0; }
  .band__accent--right { right: 0; transform: scaleX(-1); }
  .person {
    position: absolute; left: 34px; top: 34px;
  }
  .person__name { font-weight: 700; font-size: 25px; margin-bottom: 8px; }
  .line { display: flex; align-items: center; gap: 9px; font-size: 15px; margin-top: 5px; }
  .line svg { width: 14px; height: 14px; flex: none; }
  .company-contact {
    position: absolute; right: 34px; top: 38px; text-align: right;
  }
  .company-contact .line { justify-content: flex-end; font-size: 16px; }

  /* ---------- General card (back) ---------- */
  .card--general {
    left: 470px; top: 585px;
    background: radial-gradient(ellipse at 70% 20%, var(--azure-light) 0%, var(--azure) 45%, #1a5fae 100%);
    color: var(--white);
  }
  .card--general .brand { left: 110px; top: 60px; }
  .card--general .brand__disc {
    width: 150px; height: 150px;
    background: radial-gradient(circle at 60% 40%, var(--azure-light), var(--navy));
    border: 3px solid var(--white);
  }
  .card--general .brand__name { color: var(--white); font-size: 72px; }
  .card--general .brand__rule { background: var(--white); width: 360px; }
  .card--general .brand__tagline { color: var(--white); font-size: 19px; }
</style>
</head>
<body>

<section class="card card--staff" aria-label="Staff business card">
  <div class="makers">
    <span>Velmora</span>
    <span>Tovalo</span>
    <span>Orek</span>
  </div>

  <div class="brand">
    <div class="brand__disc"></div>
    <div class="brand__text">
      <div class="brand__name">HARLOW</div>
      <div class="brand__rule"></div>
      <div class="brand__tagline">ACCIDENT REPAIR CENTRE</div>
    </div>
  </div>

  <div class="band">
    <svg class="band__accent band__accent--left" viewBox="0 0 120 22" preserveAspectRatio="none">
      <path d="M0 0 H120 V8 L100 8 L94 14 L86 8 H0 Z" fill="var(--orange)"/>
    </svg>
    <svg class="band__accent band__accent--right" viewBox="0 0 120 22" preserveAspectRatio="none">
      <path d="M0 0 H120 V8 L100 8 L94 14 L86 8 H0 Z" fill="var(--orange)"/>
    </svg>

    <div class="person">
      <div class="person__name">Your Name</div>
      <div class="line">
        <svg viewBox="0 0 14 14"><rect x="3" y="1" width="8" height="12" rx="1.5" fill="none" stroke="#fff" stroke-width="1.4"/></svg>
        <span>00 123 4567</span>
      </div>
      <div class="line">
        <svg viewBox="0 0 14 14"><rect x="1" y="3" width="12" height="8" fill="#fff"/><path d="M1 3 L7 8 L13 3" fill="none" stroke="var(--navy)" stroke-width="1.2"/></svg>
        <span>name@yourweb.com</span>
      </div>
    </div>

    <div class="company-contact">
      <div class="line">
        <span>88 98 4321</span>
        <svg viewBox="0 0 14 14"><circle cx="7" cy="7" r="6" fill="none" stroke="#fff" stroke-width="1.3"/><path d="M5 4 C4 6 6 9 9 10" fill="none" stroke="#fff" stroke-width="1.5"/></svg>
      </div>
      <div class="line">
        <span>info@yourweb.com</span>
        <svg viewBox="0 0 14 14"><rect x="1" y="3" width="12" height="8" fill="#fff"/><path d="M1 3 L7 8 L13 3" fill="none" stroke="var(--navy)" stroke-width="1.2"/></svg>
      </div>
      <div class="line">
        <span>Your Address details is Here</span>
        <svg viewBox="0 0 14 14"><path d="M7 13 C3 8 2.5 6.5 2.5 5 A4.5 4.5 0 0 1 11.5 5 C11.5 6.5 11 8 7 13 Z" fill="#fff"/><circle cx="7" cy="5" r="1.6" fill="var(--navy)"/></svg>
      </div>
    </div>
  </div>
</section>

<section class="card card--general" aria-label="General business card">
  <div class="brand">
    <div class="brand__disc"></div>
    <div class="brand__text">
      <div class="brand__name">HARLOW</div>
      <div class="brand__rule"></div>
      <div class="brand__tagline">ACCIDENT REPAIR CENTRE</div>
    </div>
  </div>
</section>

</body>
</html>
```